Swiss Injection Molding Company needs a 4-page Flyer

Valmer Plastro is a injection molding company based in Zurich, Switzerland. We are looking for a new 4-page Flyer to present our company, our services and our USPs to potential customers.

For more information, see the Briefing in the uploads

Font styles to use
Sans Serif

Colors
F0912C
F2A743
F7CA91
FBE8D2
FDF5EE

```html
<!DOCTYPE html>
<html lang="en">
<head>
<meta charset="utf-8">
<title>Valmer Plastro – Flyer</title>
<link href="https://fonts.googleapis.com/css2?family=Roboto+Condensed:ital,wght@0,300;0,400;0,700;1,700&display=swap" rel="stylesheet">
<style>
:root{
  --orange:#f15a29;
  --salmon:#f8b49a;
  --dark:#353535;
  --white:#ffffff;
  --backdrop:#7b7b7b;
  --text:#1e1e1e;
  --red:#e2231a;
  --grey:#6a6a6a;
}
*{margin:0;padding:0;box-sizing:border-box}
html,body{width:875px;height:1200px;overflow:hidden;background:var(--white)}
body{font-family:"Roboto Condensed",Arial,sans-serif;color:var(--text)}
.stage{position:absolute;left:0;top:0;width:960px;height:1316px;transform:scale(0.91146);transform-origin:0 0}
.backdrop{position:absolute;left:0;top:0;width:960px;height:1162px;background:var(--backdrop)}
.spread{position:absolute;left:109px;width:742px;overflow:hidden;background:var(--white);box-shadow:0 6px 14px rgba(0,0,0,.35)}
.spread-cover{top:32px;height:524px}
.spread-inside{top:582px;height:525px}
.spread svg.shapes{position:absolute;left:0;top:0}
.abs{position:absolute}
h2.block-title{font-size:17px;font-weight:700;line-height:1;text-transform:uppercase;letter-spacing:.2px}
ul.plain{list-style:none}
ul.plain li{position:relative;padding-left:25px;font-weight:300;font-size:11.2px;line-height:13.6px}
ul.plain li::before{content:"•";position:absolute;left:2px}
.partners{top:285px;left:26px;width:320px;display:flex;justify-content:space-between;align-items:center}
.partner{font-size:12px;font-weight:700;color:#1d5fa8;display:flex;align-items:center;gap:4px}
.partner .dot{width:8px;height:8px;background:#1d5fa8}
.contact{left:26px;top:396px;color:var(--white)}
.contact h3{font-size:16px;font-weight:700;margin-bottom:18px}
.contact p{font-size:11.3px;font-weight:300;line-height:14px}
.socials{left:270px;top:476px;color:var(--white);font-size:9px;font-weight:400;display:flex;gap:10px}
.cover-title{left:397px;top:333px;color:var(--white);font-size:29px;font-weight:700;line-height:32px;letter-spacing:.2px}
.tagline{left:371px;top:426px;width:210px;height:16px;background:var(--dark);color:var(--white);font-size:8.8px;font-weight:700;padding:2px 0 0 26px}
.cover-list{left:397px;top:450px;color:var(--white);font-size:8.6px;font-weight:300;line-height:10.6px}
.usp-box{left:644px;top:440px;width:72px;height:52px;background:var(--dark);border-radius:7px;color:var(--white);font-size:9px;text-align:center;padding-top:6px}
.usp-badges{display:flex;justify-content:center;gap:6px;margin-top:3px}
.usp-badges span{width:24px;height:24px;border-radius:50%}
.badge-swiss{background:var(--red);border:2px solid var(--white)}
.badge-iso{background:var(--grey);border:1.5px solid #bbb}
.cover-bar{left:401px;top:511px;width:196px;height:13px;background:var(--white)}
.section-title{font-size:30px;font-weight:700;font-style:italic;color:var(--orange);line-height:1}
.range{left:21px;color:var(--white);width:320px}
.range h4,.service h4{font-size:12.6px;font-weight:700;text-transform:uppercase;line-height:14px}
.range ul.plain li,.service ul.plain li{font-size:9.3px;line-height:11.6px}
.range ul.plain li::before,.service ul.plain li::before{left:4px}
.service{left:394px;color:var(--white);width:320px}
.photo{top:435px;height:90px}
</style>
</head>
<body>
<div class="stage">
  <div class="backdrop"></div>

  <!-- Cover spread: back page + front page -->
  <section class="spread spread-cover">
    <svg class="shapes" width="742" height="524" viewBox="0 0 742 524">
      <rect x="371" y="0" width="371" height="524" fill="var(--orange)"/>
      <circle cx="581" cy="133" r="182" fill="var(--salmon)"/>
      <circle cx="590" cy="116" r="162" fill="#eeeeee" role="img" aria-label="Photo of injection molded plastic parts, connectors and colored granules"/>
      <path d="M0,343 C90,296 260,292 371,410 L371,524 L0,524 Z" fill="var(--orange)"/>
      <path d="M0,356 C95,312 255,312 371,432 L371,524 L0,524 Z" fill="var(--dark)"/>
    </svg>

    <div class="abs" style="left:26px;top:37px">
      <h2 class="block-title">About us</h2>
      <ul class="plain">
        <li>30 employees</li>
        <li>25 injection molding machines</li>
        <li>In-house toolmaking</li>
        <li>ISO 9001 certified</li>
        <li>Former Limmat Institute startup</li>
      </ul>
    </div>

    <div class="abs" style="left:26px;top:152px;width:320px">
      <h2 class="block-title">Your benefits</h2>
      <ul class="plain">
        <li>Quality «Made in Switzerland» Highest Precision thanks to Swiss production</li>
        <li>Fastest delivery times Shorter time-to-market and more iteration options</li>
        <li>One-Stop-Shop Seamless partner from the first prototype to series production</li>
      </ul>
    </div>

    <div class="abs partners">
      <span class="partner">Doralock</span>
      <span class="partner">Berix</span>
      <span class="partner">Sonalis</span>
      <span class="partner">Halvern Med</span>
    </div>

    <div class="abs contact">
      <h3>Contact</h3>
      <p>Valmer Plastro AG &nbsp;| &nbsp;Lindenweg 12 &nbsp;| 8045 Zurich &nbsp;| Switzerland</p>
      <p>valmer@plastro.ch &nbsp;| &nbsp;+41 44 555 01 23</p>
    </div>
    <div class="abs socials"><span>Linkfold</span><span>Pixroll</span></div>

    <h1 class="abs cover-title">SWISS INJECTION<br>MOLDING EXPERTS</h1>
    <div class="abs tagline">Your partner for complex plastic solutions:</div>
    <div class="abs cover-list">
      Injection molded prototypes within a few days<br>
      (Micro) injection molding with in-house toolmaking<br>
      Overmolding and custom solutions<br>
      Connectors and cable assemblies
    </div>
    <div class="abs usp-box">USPs
      <div class="usp-badges"><span class="badge-swiss"></span><span class="badge-iso"></span></div>
    </div>
    <div class="abs cover-bar"></div>
  </section>

  <!-- Inside spread -->
  <section class="spread spread-inside">
    <svg class="shapes" width="742" height="525" viewBox="0 0 742 525">
      <path d="M0,118 C110,62 300,58 440,120 L440,525 L0,525 Z" fill="var(--orange)"/>
      <path d="M403,0 L742,0 L742,435 L371,435 C332,300 338,120 403,0 Z" fill="var(--dark)"/>
      <defs>
        <linearGradient id="photoTone" x1="0" y1="0" x2="1" y2="1">
          <stop offset="0" stop-color="#8a9aa3"/><stop offset="1" stop-color="#3f5a3a"/>
        </linearGradient>
      </defs>
      <rect class="photo" x="371" y="435" width="110" height="90" fill="url(#photoTone)" role="img" aria-label="Photo of an engineer working on CAD design at a workstation"/>
      <rect class="photo" x="483" y="435" width="123" height="90" fill="url(#photoTone)" role="img" aria-label="Photo of two team members reviewing a 3D model on screen"/>
      <rect class="photo" x="608" y="435" width="134" height="90" fill="#9a9d9c" role="img" aria-label="Photo of a technician operating a measuring machine"/>
    </svg>

    <h2 class="abs section-title" style="left:24px;top:24px">Technology Range</h2>

    <div class="abs range" style="top:130px">
      <h4>Injection molded prototypes</h4>
      <ul class="plain">
        <li>Speed – prototypes in the original material within a few days</li>
        <li>Material selection – over 600 materials in stock: from PP to PEEK, from TPEs to silicone</li>
        <li>Flexibility – we injection mold small series of 1–100 pieces on specially developed prototype machines</li>
      </ul>
    </div>
    <div class="abs range" style="top:216px">
      <h4>(Micro) injection molding</h4>
      <ul class="plain">
        <li>Toolmaking – We produce complex molds in-house, including slides, polished and eroded surfaces</li>
        <li>Capacity – We manufacture series of 100 to 1,000,000 pieces in our modern machine park</li>
        <li>Precision – Tolerances in the hundredths range and component weights below 0.1 grams are part of our everyday business</li>
      </ul>
    </div>
    <div class="abs range" style="top:314px">
      <h4>Overmolding and custom solutions</h4>
      <ul class="plain">
        <li>Material connections – Overmolding of glass, ceramic, metal, or plastic parts</li>
        <li>Integration – Reliable embedding of electronics, sensors, or LEDs directly into the injection molded part</li>
        <li>Protection &amp; function – Special processes ensure stability, tightness, and long service life</li>
      </ul>
    </div>
    <div class="abs range" style="top:412px">
      <h4>Connectors and cable solutions</h4>
      <ul class="plain">
        <li>Customized – development of individual connectors tailored to your requirements, even for small series</li>
        <li>Everything from a single source – cable assembly and overmolding completely in-house in Zurich</li>
        <li>Reliability – robust, tight, and durable solutions for the most demanding environments</li>
      </ul>
    </div>

    <h2 class="abs section-title" style="left:394px;top:37px">Service</h2>

    <div class="abs service" style="top:87px">
      <h4>Idea</h4>
      <ul class="plain">
        <li>Engineering and design – We support you from the initial idea onwards with our many years of experience in design and optimization</li>
        <li>Material selection – With over 600 materials in stock and expertise from 1,000 applications, we help you select the right plastic</li>
      </ul>
    </div>
    <div class="abs service" style="top:162px">
      <h4>Evaluation</h4>
      <ul class="plain">
        <li>Prototyping – Using a rapid tooling process developed at Limmat Institute, we can implement your ideas in near-series production within a very short time</li>
        <li>Iterations – Variants and design ideas can be tested quickly and easily until the optimal solution is found</li>
      </ul>
    </div>
    <div class="abs service" style="top:249px">
      <h4>Pre-series</h4>
      <ul class="plain">
        <li>Toolmaking – Thanks to our in-house toolmaking facility, high-precision components can be produced and tested in the shortest possible time</li>
        <li>3D printing – For prototypes or small series, we use additive processes as a flexible supplement to injection molding</li>
      </ul>
    </div>
    <div class="abs service" style="top:324px">
      <h4>Production</h4>
      <ul class="plain">
        <li>100% Made in Switzerland – All our products are produced and tested entirely in-house in Zurich. With quality that is ISO 9001 certified</li>
        <li>Broad industry support – Thanks to our customers, we are familiar with the requirements of a wide range of industries. These include the mechanical and electrical engineering industries, the pharmaceutical industry, medical and laboratory technology, aviation, and many more</li>
      </ul>
    </div>
  </section>
</div>
</body>
</html>
```